TopQuizLane needs a dashboard page designed

Redesign the dashboard shown in the provided images.

There are two images:

NOTE: The vocabulary navigation on the left will be a very long list of words 100s, so keep that in mind when you're designing both the vocab navigation and the expanded vocab popup.

In the dashboard.png picture, there needs to be a progress chart showing the word progress like the following: review 1(show it as completed) -> review 2(show the user they are here) -> review 3(unvisited) -> review 4(unvisited)

The do-not-design-this-page.png image is for your reference only. It is not to be designed. Use it to understand the overall look and feel of the website to help you create the best dashboard page possible.
Updates

Need extra days to review

Industry/Entity Type

Education English learning

Number of Pages Required

1 page

Requirements
Must have
• The main navigation and main header cannot change between pages. See the do-not-design page for the main navigateion and header.
Should not have
• Do not add a person profile. We will not have images of our users. Keep the icons in the main navigation as they are.

```html
<!DOCTYPE html>
<html lang="en">
<head>
<meta charset="utf-8">
<title>TopQuizLane – Dashboard</title>
<link href="https://fonts.googleapis.com/css2?family=Roboto:wght@400;500;700&family=Lexend:wght@400;500&display=swap" rel="stylesheet">
<style>
:root{
  --stage:#4f4b4a;
  --shell:#2e333a;
  --shell-active:#3c424a;
  --page:#eef4fc;
  --card:#ffffff;
  --ink:#1c1c1c;
  --muted:#8a8f96;
  --line:#e3e6ea;
  --blue:#1a73e8;
  --blue-soft:#e6efff;
  --grey-dot:#d3d6da;
  --yellow:#e1be00;
  --yellow-btn:#f7c51a;
  --green:#22c55e;
  --band-lt:#e8eef8;
  --band-wm:#edf5ea;
  --band-st:#fdfbe6;
  --band-fm:#f1f1f1;
  --bar:#2c62b8;
}
*{box-sizing:border-box;margin:0;padding:0}
html,body{width:718px;height:1200px;overflow:hidden;background:var(--stage)}
body{font-family:"Roboto",sans-serif;color:var(--ink)}
.stage{position:absolute;left:0;top:0;width:1484px;height:2480px;transform:scale(.48383);transform-origin:0 0}
.screen{position:absolute;left:66px;width:1353px;height:1129px;background:var(--page);overflow:hidden}
.screen--one{top:67px}
.screen--two{top:1285px}
.abs{position:absolute}

.topbar{left:0;top:0;width:1353px;height:42px;background:var(--shell);color:#fff}
.topbar__title{position:absolute;left:0;right:0;top:13px;text-align:center;font-size:13px}
.topbar__title svg{vertical-align:middle;margin-left:6px}
.topbar__icons{position:absolute;right:22px;top:12px;display:flex;gap:20px;align-items:center}

.rail{left:0;top:42px;width:80px;height:1087px;background:var(--shell);color:#fff}
.rail__item{position:absolute;left:0;width:80px;height:73px;text-align:center;font-size:9.5px;padding-top:20px}
.rail__item svg{display:block;margin:0 auto 5px}
.rail__item--active{background:var(--shell-active)}

.vocab{left:80px;top:42px;width:157px;height:1087px;background:var(--card)}
.field{position:absolute;left:7px;width:143px;height:26px;border:1px solid var(--line);border-radius:3px;font-size:10px;padding:7px 10px;display:flex;justify-content:space-between;align-items:center}
.field--search{background:#f5f7fa;color:var(--muted);justify-content:flex-start;gap:6px}
.vocab__group{position:absolute;left:17px;top:108px;width:124px;font-size:9.5px;color:#555;display:flex;justify-content:space-between}
.vocab__rule{position:absolute;left:7px;top:100px;width:143px;height:1px;background:var(--line)}
.vocab__list{position:absolute;left:25px;top:130px;width:107px;list-style:none}
.vocab__list li{height:24px;font-size:9.5px;color:#666;display:flex;align-items:center;gap:6px;padding-left:5px}
.vocab__list li::before{content:"";width:10px;height:10px;border-radius:50%;background:var(--grey-dot)}
.vocab__list li.is-current{background:var(--blue-soft);color:#000;font-weight:700}
.vocab__list li.is-current::before{background:var(--blue)}
.vocab__more{position:absolute;left:25px;width:107px;height:17px;background:var(--yellow-btn);border-radius:2px;font-size:9px;font-weight:700;padding:3px 5px;display:flex;justify-content:space-between;align-items:center}

.card{position:absolute;background:var(--card)}
.stepper{left:266px;top:58px;width:701px;height:80px}
.stepper__line{position:absolute;top:23px;height:2px;background:#d8dbe0}
.stepper__line--done{background:var(--blue)}
.step{position:absolute;top:16px;width:90px}
.step__dot{width:16px;height:16px;border-radius:50%;background:#cfd2d6}
.step--on .step__dot{background:var(--blue)}
.step__tag{font-size:4.5px;color:#aaa;margin-top:5px}
.step__name{font-size:6.5px;color:#bbb;margin-top:1px}
.step--on .step__name{color:#111;font-weight:500}
.step__pill{display:inline-block;font-size:4.5px;padding:2px 6px;border-radius:5px;background:#d9dbde;color:#fff;margin-top:5px;min-width:44px;text-align:center}
.step__pill--now{background:#cfe0ff;color:var(--blue)}
.step__pill--done{background:#cfe0ff;color:var(--blue)}

.study{left:266px;top:154px;width:701px;height:487px}
.card__title{position:absolute;left:21px;font-family:"Lexend",sans-serif;font-weight:500;font-size:15px;color:#222}
.card__chev{position:absolute}
.word{position:absolute;left:21px;top:62px;font-size:21px;font-weight:500;display:flex;align-items:center;gap:8px}
.tabs{position:absolute;left:21px;top:105px;width:659px;height:24px;border-bottom:1px solid var(--line);display:flex;gap:28px;font-size:10.5px;color:#888}
.tabs span{height:24px}
.tabs .is-active{color:#111;font-weight:500;border-bottom:2px solid #111}
.study__text{position:absolute;left:21px;width:650px;font-size:10.5px;line-height:16.5px}
.study__head{position:absolute;left:21px;font-size:13px;font-weight:500}
.example{position:absolute;left:21px;width:650px;display:flex;gap:10px;font-size:10.5px;line-height:16.5px}
.example svg{flex:none;margin-top:4px}
.btn{position:absolute;left:21px;height:28px;background:#000;color:#fff;font-size:10.5px;font-weight:500;padding:8px 11px;border-radius:2px}

.memory{left:984px;width:343px}
.memory--wm{top:58px;height:298px}
.memory--lt{top:373px;height:271px}
.memory__list{position:absolute;left:26px;top:59px;list-style:none}
.memory__list li{height:29.4px;font-size:9.5px;color:#666;display:flex;align-items:center;gap:6px}
.memory__list li::before{content:"";width:10px;height:10px;border-radius:50%;background:var(--yellow)}
.memory--lt .memory__list li::before{background:var(--green)}
.scroll{position:absolute;left:327px;width:3px;background:#dfe2e6;border-radius:2px}
.scroll__thumb{width:3px;background:var(--blue);border-radius:2px}

.curve{left:266px;top:661px;width:1059px;height:452px}
.curve__chart{position:absolute;left:0;top:0}
.analysis__head{position:absolute;left:21px;top:262px;font-family:"Lexend",sans-serif;font-weight:500;font-size:14px}
.analysis__text{position:absolute;left:21px;top:292px;width:1000px;font-family:"Lexend",sans-serif;font-size:14.5px;line-height:22.5px;color:#222}
</style>
</head>
<body>
<div class="stage">

<!-- ============ SCREEN: REVIEW 1 ============ -->
<section class="screen screen--one">
  <header class="abs topbar">
    <div class="topbar__title">TopQuizLane<svg width="11" height="7" viewBox="0 0 11 7"><path d="M1 1l4.5 4.5L10 1" stroke="#fff" stroke-width="2" fill="none"/></svg></div>
    <div class="topbar__icons">
      <svg width="16" height="16" viewBox="0 0 16 16"><circle cx="8" cy="8" r="5" fill="none" stroke="#fff" stroke-width="3.5" stroke-dasharray="2.6 1.3"/><circle cx="8" cy="8" r="3.4" fill="#fff"/><circle cx="8" cy="8" r="1.6" fill="#2e333a"/></svg>
      <svg width="14" height="16" viewBox="0 0 14 16"><path d="M1 1h8l4 4v10H1z" fill="#fff"/><path d="M4 10h6M4 12.5h6" stroke="#2e333a" stroke-width="1.2"/></svg>
      <svg width="24" height="16" viewBox="0 0 24 16"><circle cx="8" cy="8" r="7" fill="#fff"/><circle cx="8" cy="6" r="2.5" fill="#2e333a"/><path d="M3.5 12.5c2-3 7-3 9 0" fill="#2e333a"/><path d="M18 7l2.5 2.5L23 7" stroke="#fff" stroke-width="1.3" fill="none"/></svg>
    </div>
  </header>

  <nav class="abs rail">
    <div class="rail__item rail__item--active" style="top:0"><svg width="16" height="14" viewBox="0 0 16 14"><path d="M8 0L0 7h2v7h4.5V9.5h3V14H14V7h2z" fill="#fff"/></svg>TopQuizLane</div>
    <div class="rail__item" style="top:73px"><svg width="18" height="14" viewBox="0 0 18 14"><path d="M0 2l5-2 5 2 5-2v12l-5 2-5-2-5 2z" fill="#fff"/><path d="M5 0v12M10 2v12" stroke="#2e333a" stroke-width="1"/></svg>Daily English</div>
    <div class="rail__item" style="top:146px"><svg width="13" height="16" viewBox="0 0 13 16"><rect width="13" height="16" fill="#fff"/><g fill="#2e333a"><rect x="2.5" y="2.5" width="2" height="2"/><rect x="8.5" y="2.5" width="2" height="2"/><rect x="2.5" y="6.5" width="2" height="2"/><rect x="8.5" y="6.5" width="2" height="2"/><rect x="5" y="11" width="3" height="5"/></g></svg>Business</div>
  </nav>

  <aside class="abs vocab">
    <div class="field" style="top:13px">All Category<svg width="8" height="5" viewBox="0 0 8 5"><path d="M1 1l3 3 3-3" stroke="#333" fill="none"/></svg></div>
    <div class="field field--search" style="top:57px"><svg width="10" height="10" viewBox="0 0 10 10"><circle cx="4" cy="4" r="3" stroke="#333" stroke-width="1.6" fill="none"/><path d="M6.3 6.3L9 9" stroke="#333" stroke-width="1.8"/></svg>Search here</div>
    <div class="vocab__rule"></div>
    <div class="vocab__group">Daily Words<span>›</span></div>
    <ul class="vocab__list">
      <li class="is-current">Grab</li><li>Eat</li><li>Drive</li><li>Cool Down</li><li>Crave</li><li>Go-To</li>
      <li>In The Mood For</li><li>In The Mood For</li><li>In The Mood For</li><li>In The Mood For</li><li>In The Mood For</li><li>In The Mood For</li>
      <li>In The Mood For</li><li>In The Mood For</li><li>In The Mood For</li><li>In The Mood For</li><li>In The Mood For</li><li>In The Mood For</li>
      <li>In The Mood For</li><li>In The Mood For</li><li>In The Mood For</li><li>In The Mood For</li><li>In The Mood For</li><li>In The Mood For</li>
      <li>Sip</li><li>Soothing</li><li>Stick With</li>
    </ul>
    <div class="vocab__more" style="top:779px">+240 more<svg width="10" height="10" viewBox="0 0 10 10"><circle cx="5" cy="5" r="5" fill="#fff"/><path d="M4 3l2 2-2 2" stroke="#333" fill="none"/></svg></div>
  </aside>

  <div class="card stepper">
    <div class="stepper__line" style="left:38px;width:176px"></div>
    <div class="stepper__line" style="left:244px;width:176px"></div>
    <div class="stepper__line" style="left:450px;width:176px"></div>
    <div class="step step--on" style="left:15px"><div class="step__dot"></div><div class="step__tag">REVIEW 1</div><div class="step__name">Short-Term Memory</div><span class="step__pill step__pill--now">In Progress</span></div>
    <div class="step" style="left:221px"><div class="step__dot"></div><div class="step__tag">REVIEW 2</div><div class="step__name">Working Memory</div><span class="step__pill">Not yet visited</span></div>
    <div class="step" style="left:427px"><div class="step__dot"></div><div class="step__tag">REVIEW 3</div><div class="step__name">Long-Term Memory</div><span class="step__pill">Not yet visited</span></div>
    <div class="step" style="left:633px"><div class="step__dot"></div><div class="step__tag">REVIEW 4</div><div class="step__name">Completed</div><span class="step__pill">Not yet visited</span></div>
  </div>

  <article class="card study">
    <h2 class="card__title" style="top:24px">Short-Term Memory</h2>
    <svg class="card__chev" style="left:669px;top:31px" width="10" height="6" viewBox="0 0 10 6"><path d="M1 1l4 4 4-4" stroke="#555" stroke-width="1.5" fill="none"/></svg>
    <div class="word"><svg width="24" height="23" viewBox="0 0 24 23"><path d="M12 0l3.5 7.5 8.2.9-6.1 5.6 1.7 8.1L12 18l-7.3 4.1 1.7-8.1L.3 8.4l8.2-.9z" fill="#f7c51a"/></svg>Grab</div>
    <div class="tabs"><span class="is-active">Defination</span><span>Working Memory</span><span>Long-Term Memory</span></div>
    <p class="study__text" style="top:143px">The word <b>“grab”</b> is commonly used as a verb, meaning to take something quickly or suddenly.</p>
    <h3 class="study__head" style="top:173px">Example:</h3>
    <div class="example" style="top:205px"><svg width="11" height="9" viewBox="0 0 11 9"><path d="M0 4.5h10M6 1l4 3.5L6 8" stroke="#333" fill="none"/></svg><p>Imagine you’re running late for school. You don’t have time for breakfast, so you quickly <b>grab</b> an apple from the kitchen and rush out the door.</p></div>
    <div class="example" style="top:247px"><svg width="11" height="9" viewBox="0 0 11 9"><path d="M0 4.5h10M6 1l4 3.5L6 8" stroke="#333" fill="none"/></svg><p>As you reach the buss stop, your friend waves and says, “Hey! Let’s <b>grab</b> a coffee after class.</p></div>
    <div class="example" style="top:281px"><svg width="11" height="9" viewBox="0 0 11 9"><path d="M0 4.5h10M6 1l4 3.5L6 8" stroke="#333" fill="none"/></svg><p>Later, When you sit down, your phone starts ringing. You grab it from your bag and answer.</p></div>
    <div class="btn" style="top:341px">Add to Working Memory</div>
  </article>

  <aside class="card memory memory--wm">
    <h2 class="card__title" style="top:25px">Working Memory</h2>
    <svg class="card__chev" style="left:313px;top:31px" width="10" height="6" viewBox="0 0 10 6"><path d="M1 1l4 4 4-4" stroke="#555" stroke-width="1.5" fill="none"/></svg>
    <ul class="memory__list"><li>Eat</li><li>Drive</li><li>Cool Down</li><li>Crave</li><li>Go-To</li><li>In The Mood For</li><li>In The Mood For</li><li>In The Mood For</li></ul>
    <div class="scroll" style="top:53px;height:232px"><div class="scroll__thumb" style="height:78px"></div></div>
  </aside>
  <aside class="card memory memory--lt">
    <h2 class="card__title" style="top:25px">Long-Term Memory</h2>
    <svg class="card__chev" style="left:313px;top:31px" width="10" height="6" viewBox="0 0 10 6"><path d="M1 1l4 4 4-4" stroke="#555" stroke-width="1.5" fill="none"/></svg>
    <ul class="memory__list"><li>Drive</li><li>Crave</li><li>Go-To</li><li>In The Mood For</li><li>In The Mood For</li><li>In The Mood For</li><li>In The Mood For</li></ul>
    <div class="scroll" style="top:53px;height:202px"><div class="scroll__thumb" style="height:108px"></div></div>
  </aside>

  <section class="card curve">
    <svg class="curve__chart" width="1059" height="240" viewBox="0 0 1059 240">
      <text x="21" y="39" font-family="Lexend,sans-serif" font-weight="500" font-size="15" fill="#222">Learning Curve Graph</text>
      <path d="M1026 31l4 4 4-4" stroke="#555" stroke-width="1.5" fill="none"/>
      <rect x="23" y="50" width="975" height="182" fill="#f7f7f7"/>
      <rect x="38" y="54" width="925" height="41" fill="var(--band-lt)"/>
      <rect x="38" y="95" width="925" height="80" fill="var(--band-wm)"/>
      <rect x="38" y="175" width="925" height="19" fill="var(--band-st)"/>
      <rect x="38" y="194" width="925" height="23" fill="var(--band-fm)"/>
      <g font-size="7.5" fill="#777" font-family="Roboto,sans-serif">
        <text x="49" y="75">Long-Term Memory</text>
        <text x="49" y="135">Working Memory</text>
        <text x="49" y="186">Short-Term Memory</text>
        <text x="49" y="206">Forgotten Memory</text>
      </g>
      <rect x="123" y="180" width="15" height="37" fill="var(--bar)"/>
      <rect x="215" y="95" width="16" height="122" fill="var(--bar)"/>
      <path d="M143 177C175 185 200 198 213 212" stroke="#555" stroke-width="1.2" stroke-dasharray="1.5 2.5" fill="none"/>
      <path d="M231 95C260 100 290 102 308 107C340 118 370 150 406 214" stroke="#555" stroke-width="1.2" stroke-dasharray="1.5 2.5" fill="none"/>
      <rect x="96" y="164" width="47" height="16" rx="2" fill="#fff" stroke="#ddd"/>
      <text x="119.5" y="175" text-anchor="middle" font-size="7.5" fill="#222">May 18</text>
      <rect x="179" y="83" width="45" height="16" rx="2" fill="#fff" stroke="#ddd"/>
      <text x="201.5" y="94" text-anchor="middle" font-size="7.5" fill="#222">May 19</text>
      <path d="M22 217H972" stroke="#333"/>
      <g stroke="#333"><path d="M38 217v5M84 217v5M130 217v5M176 217v5M222 217v5M268 217v5M314 217v5M360 217v5M406 217v5M452 217v5M498 217v5M544 217v5M590 217v5M636 217v5M682 217v5M728 217v5M774 217v5M820 217v5M866 217v5M912 217v5M958 217v5"/></g>
      <g font-size="7.5" fill="#555" text-anchor="middle"><text x="52" y="234">18 May</text><text x="96" y="234">12:00</text><text x="142" y="234">19 May</text><text x="188" y="234">12:00</text><text x="234" y="234">20 May</text><text x="280" y="234">12:00</text><text x="326" y="234">21 May</text><text x="372" y="234">12:00</text><text x="418" y="234">22 May</text><text x="464" y="234">12:00</text><text x="510" y="234">23 May</text><text x="556" y="234">12:00</text><text x="602" y="234">24 May</text><text x="648" y="234">12:00</text><text x="694" y="234">25 May</text><text x="740" y="234">12:00</text><text x="786" y="234">26 May</text><text x="832" y="234">12:00</text><text x="878" y="234">27 May</text><text x="924" y="234">12:00</text><text x="955" y="234">28</text></g>
      <rect x="0" y="232" width="1059" height="8" fill="#fff"/>
    </svg>
    <h3 class="analysis__head">TopQuizLane Learning Analysis:</h3>
    <p class="analysis__text">Track your language learning progress with personalized insights. TopQuizLane analyzes your vocabulary performance, memory retention, and review history to help you focus on the words that matter most.<br>&nbsp;Visual graphs show how well you’re retaining words over time, while review history highlights strengths and areas that need more attention. Whether you’re building short-term recall or long-term fluency, TopQuizLane gives you a smarter way to learn.</p>
  </section>
</section>

<!-- ============ SCREEN: REVIEW 2 ============ -->
<section class="screen screen--two">
  <header class="abs topbar">
    <div class="topbar__title">TopQuizLane<svg width="11" height="7" viewBox="0 0 11 7"><path d="M1 1l4.5 4.5L10 1" stroke="#fff" stroke-width="2" fill="none"/></svg></div>
    <div class="topbar__icons">
      <svg width="16" height="16" viewBox="0 0 16 16"><circle cx="8" cy="8" r="5" fill="none" stroke="#fff" stroke-width="3.5" stroke-dasharray="2.6 1.3"/><circle cx="8" cy="8" r="3.4" fill="#fff"/><circle cx="8" cy="8" r="1.6" fill="#2e333a"/></svg>
      <svg width="14" height="16" viewBox="0 0 14 16"><path d="M1 1h8l4 4v10H1z" fill="#fff"/><path d="M4 10h6M4 12.5h6" stroke="#2e333a" stroke-width="1.2"/></svg>
      <svg width="24" height="16" viewBox="0 0 24 16"><circle cx="8" cy="8" r="7" fill="#fff"/><circle cx="8" cy="6" r="2.5" fill="#2e333a"/><path d="M3.5 12.5c2-3 7-3 9 0" fill="#2e333a"/><path d="M18 7l2.5 2.5L23 7" stroke="#fff" stroke-width="1.3" fill="none"/></svg>
    </div>
  </header>

  <nav class="abs rail">
    <div class="rail__item rail__item--active" style="top:0"><svg width="16" height="14" viewBox="0 0 16 14"><path d="M8 0L0 7h2v7h4.5V9.5h3V14H14V7h2z" fill="#fff"/></svg>TopQuizLane</div>
    <div class="rail__item" style="top:73px"><svg width="18" height="14" viewBox="0 0 18 14"><path d="M0 2l5-2 5 2 5-2v12l-5 2-5-2-5 2z" fill="#fff"/><path d="M5 0v12M10 2v12" stroke="#2e333a" stroke-width="1"/></svg>Daily English</div>
    <div class="rail__item" style="top:146px"><svg width="13" height="16" viewBox="0 0 13 16"><rect width="13" height="16" fill="#fff"/><g fill="#2e333a"><rect x="2.5" y="2.5" width="2" height="2"/><rect x="8.5" y="2.5" width="2" height="2"/><rect x="2.5" y="6.5" width="2" height="2"/><rect x="8.5" y="6.5" width="2" height="2"/><rect x="5" y="11" width="3" height="5"/></g></svg>Business</div>
  </nav>

  <aside class="abs vocab">
    <div class="field" style="top:13px">All Category<svg width="8" height="5" viewBox="0 0 8 5"><path d="M1 1l3 3 3-3" stroke="#333" fill="none"/></svg></div>
    <div class="field field--search" style="top:57px"><svg width="10" height="10" viewBox="0 0 10 10"><circle cx="4" cy="4" r="3" stroke="#333" stroke-width="1.6" fill="none"/><path d="M6.3 6.3L9 9" stroke="#333" stroke-width="1.8"/></svg>Search here</div>
    <div class="vocab__rule"></div>
    <div class="vocab__group">Daily Words<span>›</span></div>
    <ul class="vocab__list">
      <li class="is-current">Grab</li><li>Eat</li><li>Drive</li><li>Cool Down</li><li>Crave</li><li>Go-To</li>
      <li>In The Mood For</li><li>In The Mood For</li><li>In The Mood For</li><li>In The Mood For</li><li>In The Mood For</li><li>In The Mood For</li>
      <li>In The Mood For</li><li>In The Mood For</li><li>In The Mood For</li><li>In The Mood For</li><li>In The Mood For</li><li>In The Mood For</li>
      <li>In The Mood For</li><li>In The Mood For</li><li>In The Mood For</li><li>In The Mood For</li><li>In The Mood For</li><li>In The Mood For</li>
      <li>Sip</li><li>Soothing</li><li>Stick With</li>
    </ul>
    <div class="vocab__more" style="top:779px">+240 more<svg width="10" height="10" viewBox="0 0 10 10"><circle cx="5" cy="5" r="5" fill="#fff"/><path d="M4 3l2 2-2 2" stroke="#333" fill="none"/></svg></div>
  </aside>

  <div class="card stepper">
    <div class="stepper__line stepper__line--done" style="left:38px;width:176px"></div>
    <div class="stepper__line" style="left:244px;width:176px"></div>
    <div class="stepper__line" style="left:450px;width:176px"></div>
    <div class="step step--on" style="left:15px"><div class="step__dot"></div><div class="step__tag">REVIEW 1</div><div class="step__name">Short-Term Memory</div><span class="step__pill step__pill--done">Completed</span></div>
    <div class="step step--on" style="left:221px"><div class="step__dot"></div><div class="step__tag">REVIEW 2</div><div class="step__name">Working Memory</div><span class="step__pill step__pill--now">In Progress</span></div>
    <div class="step" style="left:427px"><div class="step__dot"></div><div class="step__tag">REVIEW 3</div><div class="step__name">Long-Term Memory</div><span class="step__pill">Not yet visited</span></div>
    <div class="step" style="left:633px"><div class="step__dot"></div><div class="step__tag">REVIEW 4</div><div class="step__name">Completed</div><span class="step__pill">Not yet visited</span></div>
  </div>

  <article class="card study">
    <h2 class="card__title" style="top:24px">Short-Term Memory</h2>
    <svg class="card__chev" style="left:669px;top:31px" width="10" height="6" viewBox="0 0 10 6"><path d="M1 1l4 4 4-4" stroke="#555" stroke-width="1.5" fill="none"/></svg>
    <div class="word"><svg width="24" height="23" viewBox="0 0 24 23"><path d="M12 0l3.5 7.5 8.2.9-6.1 5.6 1.7 8.1L12 18l-7.3 4.1 1.7-8.1L.3 8.4l8.2-.9z" fill="#f7c51a"/></svg>Grab</div>
    <div class="tabs"><span>Defination</span><span class="is-active">Working Memory</span><span>Long-Term Memory</span></div>
    <h3 class="study__head" style="top:147px">More Example:</h3>
    <div class="example" style="top:179px"><svg width="11" height="9" viewBox="0 0 11 9"><path d="M0 4.5h10M6 1l4 3.5L6 8" stroke="#333" fill="none"/></svg><p>Imagine you’re running late for school. You don’t have time for breakfast, so you quickly <b>grab</b> an apple from the kitchen and rush out the door.</p></div>
    <div class="example" style="top:221px"><svg width="11" height="9" viewBox="0 0 11 9"><path d="M0 4.5h10M6 1l4 3.5L6 8" stroke="#333" fill="none"/></svg><p>As you reach the buss stop, your friend waves and says, “Hey! Let’s <b>grab</b> a coffee after class.</p></div>
    <div class="example" style="top:255px"><svg width="11" height="9" viewBox="0 0 11 9"><path d="M0 4.5h10M6 1l4 3.5L6 8" stroke="#333" fill="none"/></svg><p>Later, When you sit down, your phone starts ringing. You grab it from your bag and answer.</p></div>
    <h3 class="study__head" style="top:293px">Practice:</h3>
    <div class="example" style="top:325px"><svg width="11" height="9" viewBox="0 0 11 9"><path d="M0 4.5h10M6 1l4 3.5L6 8" stroke="#333" fill="none"/></svg><p>Imagine you’re running late for school. You don’t have time for breakfast, so you quickly <b>grab</b> an apple from the kitchen and rush out the door.</p></div>
    <p class="study__text" style="top:397px">Are you confident enough?</p>
    <div class="btn" style="top:430px">Add to Long-Term Memory</div>
  </article>

  <aside class="card memory memory--wm">
    <h2 class="card__title" style="top:25px">Working Memory</h2>
    <svg class="card__chev" style="left:313px;top:31px" width="10" height="6" viewBox="0 0 10 6"><path d="M1 1l4 4 4-4" stroke="#555" stroke-width="1.5" fill="none"/></svg>
    <ul class="memory__list"><li>Grab</li><li>Eat</li><li>Drive</li><li>Cool Down</li><li>Crave</li><li>Go-To</li><li>In The Mood For</li><li>In The Mood For</li></ul>
    <div class="scroll" style="top:53px;height:232px"><div class="scroll__thumb" style="height:78px"></div></div>
  </aside>
  <aside class="card memory memory--lt">
    <h2 class="card__title" style="top:25px">Long-Term Memory</h2>
    <svg class="card__chev" style="left:313px;top:31px" width="10" height="6" viewBox="0 0 10 6"><path d="M1 1l4 4 4-4" stroke="#555" stroke-width="1.5" fill="none"/></svg>
    <ul class="memory__list"><li>Drive</li><li>Crave</li><li>Go-To</li><li>In The Mood For</li><li>In The Mood For</li><li>In The Mood For</li><li>In The Mood For</li></ul>
    <div class="scroll" style="top:53px;height:202px"><div class="scroll__thumb" style="height:108px"></div></div>
  </aside>

  <section class="card curve">
    <svg class="curve__chart" width="1059" height="240" viewBox="0 0 1059 240">
      <text x="21" y="39" font-family="Lexend,sans-serif" font-weight="500" font-size="15" fill="#222">Learning Curve Graph</text>
      <path d="M1026 31l4 4 4-4" stroke="#555" stroke-width="1.5" fill="none"/>
      <rect x="23" y="50" width="975" height="182" fill="#f7f7f7"/>
      <rect x="38" y="54" width="925" height="41" fill="var(--band-lt)"/>
      <rect x="38" y="95" width="925" height="80" fill="var(--band-wm)"/>
      <rect x="38" y="175" width="925" height="19" fill="var(--band-st)"/>
      <rect x="38" y="194" width="925" height="23" fill="var(--band-fm)"/>
      <g font-size="7.5" fill="#777" font-family="Roboto,sans-serif">
        <text x="49" y="75">Long-Term Memory</text>
        <text x="49" y="135">Working Memory</text>
        <text x="49" y="186">Short-Term Memory</text>
        <text x="49" y="206">Forgotten Memory</text>
      </g>
      <rect x="123" y="180" width="15" height="37" fill="var(--bar)"/>
      <rect x="215" y="95" width="16" height="122" fill="var(--bar)"/>
      <path d="M143 177C175 185 200 198 213 212" stroke="#555" stroke-width="1.2" stroke-dasharray="1.5 2.5" fill="none"/>
      <path d="M231 95C260 100 290 102 308 107C340 118 370 150 406 214" stroke="#555" stroke-width="1.2" stroke-dasharray="1.5 2.5" fill="none"/>
      <rect x="96" y="164" width="47" height="16" rx="2" fill="#fff" stroke="#ddd"/>
      <text x="119.5" y="175" text-anchor="middle" font-size="7.5" fill="#222">May 18</text>
      <rect x="179" y="83" width="45" height="16" rx="2" fill="#fff" stroke="#ddd"/>
      <text x="201.5" y="94" text-anchor="middle" font-size="7.5" fill="#222">May 19</text>
      <path d="M22 217H972" stroke="#333"/>
      <g stroke="#333"><path d="M38 217v5M84 217v5M130 217v5M176 217v5M222 217v5M268 217v5M314 217v5M360 217v5M406 217v5M452 217v5M498 217v5M544 217v5M590 217v5M636 217v5M682 217v5M728 217v5M774 217v5M820 217v5M866 217v5M912 217v5M958 217v5"/></g>
      <g font-size="7.5" fill="#555" text-anchor="middle"><text x="52" y="234">18 May</text><text x="96" y="234">12:00</text><text x="142" y="234">19 May</text><text x="188" y="234">12:00</text><text x="234" y="234">20 May</text><text x="280" y="234">12:00</text><text x="326" y="234">21 May</text><text x="372" y="234">12:00</text><text x="418" y="234">22 May</text><text x="464" y="234">12:00</text><text x="510" y="234">23 May</text><text x="556" y="234">12:00</text><text x="602" y="234">24 May</text><text x="648" y="234">12:00</text><text x="694" y="234">25 May</text><text x="740" y="234">12:00</text><text x="786" y="234">26 May</text><text x="832" y="234">12:00</text><text x="878" y="234">27 May</text><text x="924" y="234">12:00</text><text x="955" y="234">28</text></g>
      <rect x="0" y="232" width="1059" height="8" fill="#fff"/>
    </svg>
    <h3 class="analysis__head">TopQuizLane Learning Analysis:</h3>
    <p class="analysis__text">Track your language learning progress with personalized insights. TopQuizLane analyzes your vocabulary performance, memory retention, and review history to help you focus on the words that matter most.<br>&nbsp;Visual graphs show how well you’re retaining words over time, while review history highlights strengths and areas that need more attention. Whether you’re building short-term recall or long-term fluency, TopQuizLane gives you a smarter way to learn.</p>
  </section>
</section>

</div>
</body>
</html>
```